IT Services Business Card Design

We require a business card design for an IT services company called RT Program Freightworks.

We specialize in taking an organisations software and readying it for deployment to new environments (e.g. Zen qa to Zen 4). This process is termed application packaging. This is not the same as putting things in boxes but I am happy to use boxes as a pun icon ;-) This is our second step in branding, we currently have a new logo and our poor excuse of a website is next to be updated but it contains information on who we are and what we cover at rtprogramfreightworks.example

We are looking for a fun, modern but stylish and professional looking design.

I have attached the logo in multiple formats including vector formats (and the fonts that created the logo if required)
Updates

Thanks to all the designers so far, some great designs in there.  I will be selecting a card design on the deadline date. 

However, there is still time to submit some more designs.  The majority of the ones I have so far are typical simplistic designs that we have all seen before and I have enough of those to choose from now.  If you wish to submit any more designs, please submit somthing unusual to grab our attention.

Target Market(s)

Project executives of large organisations looking for Panecraft migrations

Industry/Entity Type

Software

Requirements
Must have
• Want to show company name, contact name, title, main number, contact number, fax number, email address and website address. I do not want to show the address.
Must use the attached logo, retaining the colours in them.

This has to be a double-sided design. I will be using lark.example and will be selecting their rounded corner business card design.

Their templates and design requirements (sizing etc.) can be found here: http://uk.lark.example/help/faq/templates-and-guidelines.html

Happy for company name or website to be on either side of the card.

This design has to be original and not used before for another company

Would like to style it around the business colours in the logo
Nice to have
• Lark.example has an option for multiple card designs to appear on the back. If this is possible in the budget and time you have and you have a design(s) that work with that but carry the same style and theme, that would be nice to see but not necessary.
Should not have
• We do not want to put a postal address on the cards

```html
<!DOCTYPE html>
<html lang="en">
<head>
<meta charset="utf-8">
<title>RT Program Freightworks – Business Card</title>
<link rel="stylesheet" href="https://fonts.googleapis.com/css2?family=Didact+Gothic&display=swap">
<style>
  :root {
    --bg-core: #363833;
    --bg-edge: #262824;
    --name: #dcdcdc;
    --label: #8b8d89;
    --value: #e6e6e4;
    --divider: #c9c9c7;
    --accent: #5a78e0;
  }
  html, body {
    margin: 0;
    padding: 0;
    overflow: hidden;
    background: var(--bg-edge);
  }
  .card {
    position: relative;
    width: 1200px;
    height: 805px;
    overflow: hidden;
    background: radial-gradient(ellipse 70% 65% at 45% 45%, var(--bg-core) 0%, var(--bg-edge) 100%);
    font-family: "Didact Gothic", "Century Gothic", sans-serif;
  }
  .divider {
    position: absolute;
    left: 299px;
    top: 58px;
    width: 3px;
    height: 693px;
    background: linear-gradient(to bottom, transparent 0%, var(--divider) 12%, var(--divider) 85%, transparent 100%);
  }
  .brand-initials {
    position: absolute;
    left: 106px;
    top: 138px;
    margin: 0;
    font-size: 146px;
    font-weight: 400;
    line-height: 1;
    color: var(--name);
  }
  .brand-name {
    position: absolute;
    left: 321px;
    top: 160px;
    margin: 0;
    font-size: 62px;
    font-weight: 400;
    line-height: 56px;
    color: var(--name);
  }
  .brand-mark {
    position: absolute;
    left: 690px;
    top: 130px;
  }
  .contact {
    position: absolute;
    top: 380px;
    left: 0;
    margin: 0;
    display: grid;
    grid-template-columns: 289px auto;
    column-gap: 30px;
    row-gap: 14px;
    font-size: 30px;
    line-height: 34px;
  }
  .contact dt {
    text-align: right;
    color: var(--label);
  }
  .contact dd {
    margin: 0;
    color: var(--value);
  }
</style>
</head>
<body>
  <main class="card">
    <div class="divider"></div>

    <h1 class="brand-initials" aria-hidden="true">RT</h1>
    <p class="brand-name">Program<br>Freightworks</p>
    <svg class="brand-mark" width="150" height="150" viewBox="0 0 150 150" aria-hidden="true">
      <circle cx="75" cy="75" r="72" fill="var(--accent)"/>
    </svg>

    <dl class="contact">
      <dt>contact:</dt><dd>Alex Marlow</dd>
      <dt>title:</dt><dd>Managing Director</dd>
      <dt>phone number:</dt><dd>0800 555 0142</dd>
      <dt>mobile number:</dt><dd>07700 900 142</dd>
      <dt>fax number:</dt><dd>0800 555 0187</dd>
      <dt>e-mail:</dt><dd>Enquiries@RTProgramFreightworks.example</dd>
      <dt>website:</dt><dd>http://rtprogramfreightworks.example/</dd>
    </dl>
  </main>
</body>
</html>
```